New Business Card Design*

We are a recruitment company based in Norwich/Cambridge England.
I have included our company logo which we want to remain the same.

What we are looking for is a new creative Business card which will really stand out!!

Contact Information for Business Card

Harriet Vance
email: Harriet@brelvix.co.uk
Address: Tolworth House
Ashgrove Innovation Park
Pelham Road
Norwich
KT9 3QD
Tel:01632 960418

```html
<!DOCTYPE html>
<html lang="en">
<head>
<meta charset="utf-8">
<title>Brelvix Business Card</title>
<link href="https://fonts.googleapis.com/css2?family=Roboto:wght@400;500;700&display=swap" rel="stylesheet">
<style>
  :root {
    --green: #7cbb34;
    --green-dark: #5f9a26;
    --green-light: #8cc63f;
    --grey: #8a8a8f;
    --grey-light: #c9c9cc;
    --ink: #3a3a3a;
    --paper: #ffffff;
    --paper-shade: #ececec;
    --backdrop: #e6e7e9;
  }
  * { margin: 0; padding: 0; box-sizing: border-box; }
  html, body {
    width: 1200px; height: 900px; overflow: hidden;
    background: var(--backdrop);
    font-family: "Roboto", Arial, sans-serif;
  }
  .canvas { position: relative; width: 1200px; height: 900px; }
  .card {
    position: absolute; left: 250px; width: 700px; height: 400px;
    border-radius: 22px; overflow: hidden;
    box-shadow: 0 8px 24px rgba(0,0,0,0.18);
  }
  .card-front {
    top: 40px;
    background: linear-gradient(160deg, var(--paper-shade) 0%, var(--paper) 55%);
  }
  .card-back {
    top: 470px;
    background: linear-gradient(135deg, var(--green-light) 0%, var(--green) 55%, var(--green-dark) 100%);
  }
  .wave { position: absolute; inset: 0; }
  .brand { position: absolute; display: flex; align-items: center; gap: 14px; }
  .brand-dot { width: 54px; height: 54px; border-radius: 50%; }
  .brand-name { font-size: 52px; font-weight: 500; letter-spacing: -1px; line-height: 1; }
  .brand-tagline {
    position: absolute; font-size: 11px; font-weight: 400;
    letter-spacing: 3px; text-transform: none;
  }
  .card-front .brand { left: 50px; top: 108px; }
  .card-front .brand-dot { background: var(--grey); }
  .card-front .brand-name { color: var(--green); }
  .card-front .brand-tagline { left: 118px; top: 170px; color: var(--grey); }
  .divider {
    position: absolute; left: 392px; top: 70px; width: 2px; height: 170px;
    background: var(--green);
  }
  .contact { position: absolute; left: 418px; top: 66px; color: var(--ink); }
  .contact-name { font-size: 26px; font-weight: 500; color: var(--green); }
  .contact-role { font-size: 15px; margin-top: 2px; margin-bottom: 12px; }
  .contact-address { font-size: 13px; line-height: 1.45; margin-bottom: 10px; }
  .contact-line { display: flex; align-items: center; gap: 8px; font-size: 13.5px; line-height: 1.6; }
  .contact-line svg { width: 12px; height: 12px; flex: none; }
  .accent { color: var(--green); }
  .card-back .brand { left: 190px; top: 140px; }
  .card-back .brand-dot { background: var(--grey-light); }
  .card-back .brand-name { color: var(--grey-light); font-size: 64px; }
  .card-back .brand-tagline { left: 262px; top: 218px; color: var(--grey-light); font-size: 12px; }
  .back-url {
    position: absolute; left: 0; right: 0; top: 300px; text-align: center;
    color: var(--grey-light); font-size: 16px; letter-spacing: 1px;
  }
</style>
</head>
<body>
<div class="canvas">

  <section class="card card-front">
    <svg class="wave" viewBox="0 0 700 400" preserveAspectRatio="none">
      <path d="M0,192 C120,196 200,250 300,318 S470,400 580,400 L0,400 Z" fill="var(--green)"/>
      <path d="M0,178 C120,182 205,238 305,306 S470,392 590,398" fill="none" stroke="var(--grey)" stroke-width="4"/>
    </svg>

    <div class="brand">
      <span class="brand-dot"></span>
      <span class="brand-name">Brelvix</span>
    </div>
    <div class="brand-tagline">Technology Recruitment</div>

    <div class="divider"></div>

    <div class="contact">
      <div class="contact-name">Harriet Vance</div>
      <div class="contact-role">Founder</div>
      <div class="contact-address">Tolworth House, Ashgrove Innovation Park<br>Pelham Road, Norwich KT9 3QD</div>
      <div class="contact-line">
        <svg viewBox="0 0 12 12"><path d="M3,1 L5,3.5 L4,5 Q5,7 7,8 L8.5,7 L11,9 L9.5,11 Q4,10.5 1,3 Z" fill="var(--green)"/></svg>
        <span>01632 960418</span>
      </div>
      <div class="contact-line">
        <svg viewBox="0 0 12 12"><rect x="1" y="2.5" width="10" height="7" fill="none" stroke="var(--green)" stroke-width="1.2"/><path d="M1,2.5 L6,6.5 L11,2.5" fill="none" stroke="var(--green)" stroke-width="1.2"/></svg>
        <span>Harriet@brelvix.co.uk</span>
      </div>
      <div class="contact-line">
        <svg viewBox="0 0 12 12"><circle cx="6" cy="6" r="5" fill="none" stroke="var(--green)" stroke-width="1.2"/><ellipse cx="6" cy="6" rx="2.2" ry="5" fill="none" stroke="var(--green)" stroke-width="1"/><path d="M1,6 H11" stroke="var(--green)" stroke-width="1"/></svg>
        <span>www.<span class="accent">brelvix</span>.co.uk</span>
      </div>
    </div>
  </section>

  <section class="card card-back">
    <div class="brand">
      <span class="brand-dot"></span>
      <span class="brand-name">Brelvix</span>
    </div>
    <div class="brand-tagline">Technology Recruitment</div>
    <div class="back-url">www.brelvix.co.uk</div>
  </section>

</div>
</body>
</html>
```